Etiketten-Design für Honiggläser
Zielgruppe
Imkerei Lindner
Wir sind eine Familienbetrieb und vertreiben hochwertigen Honig aus eigener Imkerei
Aufgabenstellung
Es werden Etiketten für Honiggläser benötigt
Es gibt drei verschiedene Größen von Gläser (siehe Anhang) und je größe einmal „Frühtracht“ und einmal „Sommertracht“
Also insgesamt 6 Etiketten
500g Frühtracht und Sommertracht
250g Frühtracht und Sommertracht
150g Frühtracht und Sommertracht

```html
<!DOCTYPE html>
<html lang="de">
<head>
<meta charset="utf-8">
<title>Etikett Honig Sommertracht 500g – Imkerei Lindner</title>
<link rel="stylesheet" href="https://fonts.googleapis.com/css2?family=Open+Sans:wght@400;600;700&display=swap">
<style>
  :root {
    --page-bg: #f2f2f2;
    --label-white: #ffffff;
    --honey-yellow: #f2c94a;
    --honey-orange: #e9a23c;
    --frame-grey: #c8c8c8;
    --seal-grey: #e4e4e4;
    --text-grey: #a7a7a7;
    --text-dark: #4a4a4a;
  }
  html, body {
    margin: 0;
    width: 1200px;
    height: 766px;
    overflow: hidden;
    background: var(--page-bg);
    font-family: "Open Sans", Arial, sans-serif;
  }
  .label {
    position: absolute;
    left: 30px;
    top: 233px;
    width: 1140px;
    height: 300px;
    background: var(--label-white);
  }
  .label-shape {
    position: absolute;
    inset: 0;
  }
  .brand-name {
    position: absolute;
    top: 42px;
    left: 0;
    width: 100%;
    text-align: center;
    margin: 0;
    font-size: 34px;
    line-height: 46px;
    font-weight: 600;
    letter-spacing: 2px;
    color: var(--honey-orange);
  }
  .product {
    position: absolute;
    left: 399px;
    width: 341px;
    top: 104px;
    text-align: center;
  }
  .product-name {
    margin: 0;
    font-size: 50px;
    line-height: 60px;
    font-weight: 700;
    color: var(--honey-orange);
  }
  .product-variety {
    margin: 0;
    font-size: 29px;
    line-height: 34px;
    font-weight: 700;
    color: var(--text-grey);
  }
  .product-weight {
    margin: 2px 0 0;
    font-size: 23px;
    line-height: 28px;
    font-weight: 700;
    color: var(--honey-orange);
  }
  .info-box {
    position: absolute;
    top: 120px;
    width: 230px;
    height: 162px;
    box-sizing: border-box;
    background: var(--label-white);
    border: 3px solid var(--frame-grey);
    border-radius: 12px;
    color: var(--text-dark);
  }
  .info-box--certificates {
    left: 47px;
    text-align: center;
    padding: 8px 8px 0;
  }
  .info-box--details {
    left: 862px;
    padding: 9px 12px;
    font-size: 12px;
    line-height: 14px;
  }
  .seals {
    display: flex;
    align-items: flex-start;
    justify-content: space-between;
    padding: 0 4px;
  }
  .seal {
    background: var(--seal-grey);
    border-radius: 4px;
  }
  .seal--eu { width: 98px; height: 64px; }
  .seal--national { width: 76px; height: 76px; margin-right: 4px; }
  .seal-code {
    margin: -10px 0 0;
    width: 106px;
    text-align: center;
    font-size: 12.5px;
    line-height: 16px;
  }
  .address {
    margin: 4px 0 0;
    font-size: 13px;
    line-height: 18px;
  }
  .details p { margin: 0; }
  .details .gap { margin-top: 8px; }
  .details .origin { position: absolute; bottom: 8px; left: 12px; }
</style>
</head>
<body>
  <main class="label" aria-label="Flaches Etikett Honig Sommertracht 500g">
    <svg class="label-shape" width="1140" height="300" viewBox="0 0 1140 300">
      <g role="img" aria-label="Gelbes Muster mit Waben, Bienenkörben, Blüten und Honiglöffeln">
        <rect x="0" y="101" width="1140" height="199" fill="var(--honey-yellow)"/>
      </g>
      <polygon points="399,101 740,101 668,236 474,236" fill="var(--label-white)"
               stroke="var(--frame-grey)" stroke-width="4" stroke-linejoin="round"/>
      <line x1="0" y1="101" x2="399" y2="101" stroke="var(--frame-grey)" stroke-width="3"/>
      <line x1="740" y1="101" x2="1140" y2="101" stroke="var(--frame-grey)" stroke-width="3"/>
      <rect x="397" y="98" width="345" height="5" fill="var(--label-white)"/>
    </svg>

    <h1 class="brand-name">Imkerei Lindner</h1>

    <div class="product">
      <p class="product-name">Honig</p>
      <p class="product-variety">Sommertracht</p>
      <p class="product-weight">500g</p>
    </div>

    <section class="info-box info-box--certificates">
      <div class="seals">
        <div class="seal seal--eu" role="img" aria-label="Platz für Bio-Siegel"></div>
        <div class="seal seal--national" role="img" aria-label="Platz für Bio-Siegel"></div>
      </div>
      <p class="seal-code">AT-BIO-xxx</p>
      <p class="address">Lindenweg 4, 31600 Wiesental<br>info@imkerei-lindner.de<br>www.imkerei-lindner.de</p>
    </section>

    <section class="info-box info-box--details details">
      <p>Imkerei Lindner</p>
      <p class="gap">Nettofüllmenge: 500g</p>
      <p class="gap">Lagerbedingungen<br>- dunkel, kühl und trocken<br>Mindesthaltbarkeitsdatum</p>
      <p class="origin">Deutscher Honig aus eigener Imkerei</p>
    </section>
  </main>
</body>
</html>
```